Now Open Poster

We need a banner for our sports supplement and nutritional store, Harbor Nutrition.
We were hoping for some sort of creative word art piece.
I have drawn my own mock up just to give you all a very basic starting point. But you are free to go with whatever you feel will work best.
The primary objective is simply to explain a little about what the company does, and then direct traffic towards the store with an 'Open Arrow' pointing left.
Text words we have chosen are:
Protein
Creatine
Health
Fitness
Sports Science
Nutrition
Energy
Achievement
Amino Acids
Organic
Supplements
Performance
Testosterone Support
Vitamins
Growth
Diet
Happiness
Weight Loss
Strong
Natural
Vitality
Accomplished
Below the word art we want our logo (See attached options)
Then below the logo the phrase "Success Starts Here"
Dimensions of the poster are 140cm x 60cm.
Colours: Blues/Whites/Greys/Blacks (Lots of white space please)
Here are some cool pieces I found that had some interesting elements that I liked (I'd love to see a mash-up of styles with a street art feel to it. Something funky!):
http://www.moodwall-example.com/pin/100000000000000001/
http://www.moodwall-example.com/pin/100000000000000002/
http://www.moodwall-example.com/pin/100000000000000003/
http://www.moodwall-example.com/pin/100000000000000004/
http://www.moodwall-example.com/pin/100000000000000005/
Thanks for reading, message me if you have any further questions!
- Tobias

```html
<!DOCTYPE html>
<html lang="en">
<head>
<meta charset="utf-8">
<title>Harbor Nutrition – Now Open</title>
<link rel="stylesheet" href="https://fonts.googleapis.com/css2?family=Alfa+Slab+One&family=Open+Sans:ital,wght@0,300;0,400;0,700;1,300;1,400;1,700&family=PT+Serif:wght@700&family=Yellowtail&display=swap">
<style>
  :root {
    --paper: #fdfbe8;
    --open-red: #e3202b;
    --blue-deep: #0d4f9c;
    --blue-mid: #2a86cc;
    --blue-light: #86cdef;
    --blue-violet: #4c6fbf;
    --band-blue: #1a6fb8;
    --seal-fill: #e6eff2;
    --seal-ink: #1a5a9e;
    --white: #ffffff;
    --arrow-dark: #1f7a2a;
    --arrow-mid: #3fae3a;
    --arrow-light: #b8e86a;
  }
  html, body {
    margin: 0;
    padding: 0;
    width: 1200px;
    height: 2799px;
    overflow: hidden;
    background: var(--paper);
  }
  .poster {
    display: block;
    width: 1200px;
    height: 2799px;
  }
  .open-title {
    font-family: "Alfa Slab One", "PT Serif", serif;
    fill: var(--open-red);
  }
  .word { font-family: "Open Sans", Arial, sans-serif; }
  .w-light { font-weight: 300; }
  .w-regular { font-weight: 400; }
  .w-bold { font-weight: 700; }
  .w-italic { font-style: italic; }
  .fill-a { fill: url(#word-grad-a); }
  .fill-b { fill: url(#word-grad-b); }
  .fill-c { fill: url(#word-grad-c); }
  .fill-d { fill: url(#word-grad-d); }
  .stop-deep { stop-color: var(--blue-deep); }
  .stop-mid { stop-color: var(--blue-mid); }
  .stop-light { stop-color: var(--blue-light); }
  .stop-violet { stop-color: var(--blue-violet); }
  .stop-arrow-dark { stop-color: var(--arrow-dark); }
  .stop-arrow-mid { stop-color: var(--arrow-mid); }
  .stop-arrow-light { stop-color: var(--arrow-light); }
  .brand-band { fill: var(--band-blue); }
  .motto-small, .motto-name {
    font-family: "PT Serif", Georgia, serif;
    font-weight: 700;
    fill: var(--white);
  }
  .seal-ring { fill: var(--white); }
  .seal-disc { fill: var(--seal-fill); }
  .seal-name {
    font-family: "Open Sans", Arial, sans-serif;
    font-weight: 700;
    fill: var(--seal-ink);
  }
  .tagline {
    font-family: "Yellowtail", cursive;
    fill: var(--open-red);
  }
  .tagline-swoosh {
    fill: none;
    stroke: var(--open-red);
    stroke-width: 9;
    stroke-linecap: round;
  }
</style>
</head>
<body>
<svg class="poster" viewBox="0 0 1200 2799" xmlns="http://www.w3.org/2000/svg" aria-label="Harbor Nutrition now open poster">
  <defs>
    <linearGradient id="word-grad-a" x1="0" y1="0" x2="1" y2="0">
      <stop offset="0" class="stop-violet"/>
      <stop offset="0.5" class="stop-light"/>
      <stop offset="1" class="stop-mid"/>
    </linearGradient>
    <linearGradient id="word-grad-b" x1="0" y1="0" x2="1" y2="0">
      <stop offset="0" class="stop-deep"/>
      <stop offset="0.6" class="stop-mid"/>
      <stop offset="1" class="stop-light"/>
    </linearGradient>
    <linearGradient id="word-grad-c" x1="0" y1="0" x2="1" y2="0">
      <stop offset="0" class="stop-light"/>
      <stop offset="1" class="stop-mid"/>
    </linearGradient>
    <linearGradient id="word-grad-d" x1="0" y1="0" x2="1" y2="0">
      <stop offset="0" class="stop-deep"/>
      <stop offset="0.45" class="stop-mid"/>
      <stop offset="0.7" class="stop-light"/>
      <stop offset="1" class="stop-deep"/>
    </linearGradient>
    <linearGradient id="arrow-grad" x1="0" y1="1" x2="1" y2="0">
      <stop offset="0" class="stop-arrow-light"/>
      <stop offset="0.5" class="stop-arrow-mid"/>
      <stop offset="1" class="stop-arrow-dark"/>
    </linearGradient>
  </defs>

  <!-- Headline -->
  <text class="open-title" x="200" y="292" font-size="215" textLength="790" lengthAdjust="spacingAndGlyphs">OPEN</text>

  <!-- Curved arrow pointing left toward the store -->
  <g class="open-arrow">
    <path fill="url(#arrow-grad)" d="M660 392 L810 292 L810 348 L1010 348 C1070 348 1085 300 1070 265 C1060 240 1040 228 1010 222 C1075 214 1125 250 1125 310 C1125 392 1075 440 1000 440 L810 440 L810 496 Z"/>
    <path fill="var(--arrow-dark)" opacity="0.35" d="M810 440 L1000 440 C1075 440 1125 392 1125 310 C1118 375 1075 418 1000 420 L810 420 Z"/>
  </g>

  <!-- Word art -->
  <g class="word-cloud">
    <text class="word w-bold fill-a" x="224" y="489" font-size="97" textLength="369" lengthAdjust="spacingAndGlyphs">Protein,</text>
    <text class="word w-light fill-b" x="93" y="569" font-size="93" textLength="364" lengthAdjust="spacingAndGlyphs">Creatine,</text>
    <text class="word w-bold w-italic fill-a" x="215" y="662" font-size="93" textLength="313" lengthAdjust="spacingAndGlyphs">Health,</text>
    <text class="word w-light fill-b" x="153" y="737" font-size="75" textLength="295" lengthAdjust="spacingAndGlyphs">Fitness,</text>
    <text class="word w-regular fill-d" x="93" y="821" font-size="103" textLength="706" lengthAdjust="spacingAndGlyphs">Sports Science,</text>
    <text class="word w-regular w-italic fill-c" x="575" y="914" font-size="93" textLength="399" lengthAdjust="spacingAndGlyphs">Nutrition,</text>
    <text class="word w-bold fill-b" x="504" y="1008" font-size="97" textLength="326" lengthAdjust="spacingAndGlyphs">Energy,</text>
    <text class="word w-light fill-c" x="289" y="1082" font-size="97" textLength="560" lengthAdjust="spacingAndGlyphs">Achievement,</text>
    <text class="word w-regular fill-a" x="215" y="1166" font-size="93" textLength="565" lengthAdjust="spacingAndGlyphs">Amino Acids,</text>
    <text class="word w-bold w-italic fill-b" x="116" y="1254" font-size="93" textLength="384" lengthAdjust="spacingAndGlyphs">Organic,</text>
    <text class="word w-bold fill-a" x="271" y="1343" font-size="97" textLength="643" lengthAdjust="spacingAndGlyphs">Supplements,</text>
    <text class="word w-regular w-italic fill-b" x="481" y="1437" font-size="90" textLength="555" lengthAdjust="spacingAndGlyphs">Performance,</text>
    <text class="word w-light fill-d" x="205" y="1534" font-size="93" textLength="924" lengthAdjust="spacingAndGlyphs">Testosterone Support,</text>
    <text class="word w-bold fill-b" x="93" y="1609" font-size="97" textLength="420" lengthAdjust="spacingAndGlyphs">Vitamins,</text>
    <text class="word w-bold w-italic fill-b" x="541" y="1689" font-size="90" textLength="355" lengthAdjust="spacingAndGlyphs">Growth,</text>
    <text class="word w-light fill-c" x="313" y="1758" font-size="118" textLength="247" lengthAdjust="spacingAndGlyphs">Diet,</text>
    <text class="word w-light w-italic fill-c" x="578" y="1829" font-size="90" textLength="458" lengthAdjust="spacingAndGlyphs">Happiness,</text>
    <text class="word w-bold fill-a" x="196" y="1922" font-size="100" textLength="588" lengthAdjust="spacingAndGlyphs">Weight Loss,</text>
    <text class="word w-light fill-b" x="93" y="1997" font-size="93" textLength="303" lengthAdjust="spacingAndGlyphs">Strong,</text>
    <text class="word w-bold w-italic fill-b" x="401" y="2071" font-size="93" textLength="420" lengthAdjust="spacingAndGlyphs">Natural,</text>
    <text class="word w-bold fill-d" x="93" y="2155" font-size="100" textLength="351" lengthAdjust="spacingAndGlyphs">Vitality,</text>
    <text class="word w-bold fill-b" x="446" y="2155" font-size="56" textLength="463" lengthAdjust="spacingAndGlyphs">Accomplished,</text>
  </g>

  <!-- Brand band -->
  <rect class="brand-band" x="0" y="2329" width="1200" height="209"/>
  <g class="brand-motto">
    <text class="motto-small" x="190" y="2400" font-size="50">I am</text>
    <text class="motto-name" x="120" y="2491" font-size="92" textLength="320" lengthAdjust="spacingAndGlyphs">Harbor</text>
  </g>
  <g class="brand-seal">
    <circle class="seal-ring" cx="612" cy="2435" r="142"/>
    <circle class="seal-disc" cx="612" cy="2435" r="128"/>
    <text class="seal-name" x="612" y="2425" font-size="44" text-anchor="middle">Harbor</text>
    <text class="seal-name" x="612" y="2475" font-size="34" text-anchor="middle">Nutrition</text>
  </g>

  <!-- Tagline: rising script with a swoosh running beneath it -->
  <g class="tagline-group" transform="translate(200 2712) rotate(-10)">
    <text class="tagline" x="0" y="0" font-size="108" textLength="680" lengthAdjust="spacingAndGlyphs">Success Starts Here</text>
    <path class="tagline-swoosh" d="M5 42 C300 50 600 40 770 -25"/>
  </g>
</svg>
</body>
</html>
```